Harlow Ironworks Business Card

We need a business card design for a new small metal fabrication business in rural NSW, Australia.

The business (Harlow Ironworks) is owner operated by a man with the initials KB - much of the branding comes from this name.

Harlow Ironworks designs, engineers, repairs and manufactures a range of custom, quality metal works including vehicle trays, agricultural machinery impliments, trailers, wood splitters, fire pits, furniture etc.

The brand position focuses on custom work of the highest quality.

Business card design should show quality, attention to detail and stand out among a mass of business cards.

Logos are in the files

The grey color may be changed on the logo if required to stand out more.

There is an image attached of a simple card that is liked because it is clean, clear, simple, masculine and effective. It says 'quality'. As most of the work we do is custom it would be good to have the business card speak to this.

Target Market(s)

Rural and regional based Australians. Primarily adult male 25-60 yrs. Primary production / rural / travelling lifestyle.

Industry/Entity Type

Metal Fabrication

Contact Information for Business Card

The words 'custom quality fabrications' would be great somewhere perhaps on the backside (not on the information side)
Name
title
Phone: 0418 539 746 and (02) 6193 4827
email: info@harlowiw.com.au
www.harlowiw.com.au

address (2 lines)

Requirements
Nice to have
• Background colour should be very navy blue or black.
Should not have
• NO orange and blue combinations.
• Navy is OK

```html
<!DOCTYPE html>
<html lang="en">
<head>
<meta charset="utf-8">
<title>Harlow Ironworks Business Card</title>
<link href="https://fonts.googleapis.com/css2?family=Open+Sans:wght@400;600;700&display=swap" rel="stylesheet">
<style>
  :root {
    --navy: #4a5675;
    --green: #6cbd45;
    --white: #ffffff;
    --rule: #333333;
  }
  * { margin: 0; padding: 0; box-sizing: border-box; }
  html, body {
    width: 1079px; height: 1200px; overflow: hidden;
    background: var(--white);
    font-family: "Open Sans", Arial, sans-serif;
  }
  .canvas { position: relative; width: 1079px; height: 1200px; }

  /* Front: information side */
  .card-front {
    position: absolute; left: 224px; top: 172px;
    width: 635px; height: 389px;
    border: 1px solid var(--rule);
    background: var(--white);
  }
  .info-panel {
    position: absolute; left: 287px; top: 24px;
    width: 347px; height: 364px;
    background: var(--navy);
    color: var(--white);
  }
  .base-band {
    position: absolute; left: 0; bottom: 0;
    width: 288px; height: 23px;
    background: var(--navy);
  }
  .brand-block {
    position: absolute; left: 52px; top: 98px; width: 188px;
    text-align: center;
  }
  .brand-mark {
    width: 46px; height: 46px; margin: 0 auto 22px;
    background: var(--green);
  }
  .brand-name {
    color: var(--navy); font-weight: 700;
    font-size: 25px; line-height: 1.05; letter-spacing: 1px;
  }
  .brand-rule {
    height: 1px; background: var(--navy); margin: 10px 0 4px;
  }
  .tagline {
    color: var(--navy); font-weight: 600; font-size: 12.5px;
  }

  .contact-name { position: absolute; left: 27px; top: 45px; font-size: 32px; font-weight: 600; line-height: 1; }
  .contact-title { position: absolute; left: 27px; top: 89px; font-size: 22px; font-weight: 600; line-height: 1; }
  .contact-lines {
    position: absolute; left: 27px; top: 144px;
    font-size: 18.5px; font-weight: 600; line-height: 23.8px;
    display: grid; grid-template-columns: 69px auto;
  }
  .contact-lines .full { grid-column: 1 / 3; }
  .address {
    position: absolute; left: 27px; top: 262px;
    font-size: 18.5px; font-weight: 600; line-height: 23.5px;
  }

  /* Back sides */
  .card-back {
    position: absolute; top: 735px; width: 445px; height: 272px;
    display: flex; align-items: center; justify-content: center;
  }
  .card-back.navy { left: 59px; background: var(--navy); }
  .card-back.light { left: 558px; background: var(--white); border: 1px solid var(--rule); }
  .back-lockup { display: flex; align-items: center; gap: 12px; }
  .back-mark { width: 42px; height: 42px; background: var(--green); }
  .back-name {
    font-weight: 700; font-size: 27px; line-height: 1.02; letter-spacing: 1px;
  }
  .navy .back-name { color: var(--white); }
  .light .back-name { color: var(--navy); }
</style>
</head>
<body>
<main class="canvas">
  <section class="card-front">
    <div class="brand-block">
      <div class="brand-mark"></div>
      <div class="brand-name">HARLOW<br>IRONWORKS</div>
      <div class="brand-rule"></div>
      <div class="tagline">custom quality fabrications</div>
    </div>
    <div class="base-band"></div>
    <div class="info-panel">
      <div class="contact-name">Name</div>
      <div class="contact-title">title</div>
      <div class="contact-lines">
        <span>Phone</span><span>: 0418 539 746</span>
        <span></span><span>: (02) 6193 4827</span>
        <span>email</span><span>: info@harlowiw.com.au</span>
        <span class="full">www.harlowiw.com.au</span>
      </div>
      <div class="address">Address<br>Address</div>
    </div>
  </section>

  <section class="card-back navy">
    <div class="back-lockup">
      <div class="back-mark"></div>
      <div class="back-name">HARLOW<br>IRONWORKS</div>
    </div>
  </section>

  <section class="card-back light">
    <div class="back-lockup">
      <div class="back-mark"></div>
      <div class="back-name">HARLOW<br>IRONWORKS</div>
    </div>
  </section>
</main>
</body>
</html>
```